Yoga By Mirelle Ad for print

I need a print ad designed to go in a brochure for a charity event. I've attached the specs. I need the specs for the 1/2 page ad.
Text for ad:

“E-RYT 200 extensive training with Kestrel Path
Social Media Influencer
Offering group, private and corporate yoga classes
Email: info@yogabymirelle.example
Web: www.yogabymirelle.example
Phone: 555-201-3864
Instagram: @sunlitmatcurls

Target Market(s)

Yoga practitioners and businesses looking to bring yoga in to their operation.

Font styles to use
Serif
Script

Colors
eda3c7
e34197
eea4c8
f9d9e8
feeeee
000000
1b1b1b
cbcbcb
eaeaea

Requirements
Must have
• One version of my logo, I have provided many to choose from for best aesthetic appeal

```html
<!DOCTYPE html>
<html lang="en">
<head>
<meta charset="utf-8">
<title>Yoga By Mirelle – Print Ad</title>
<link rel="stylesheet" href="https://fonts.googleapis.com/css2?family=Yellowtail&family=Roboto:wght@400;500;700&display=swap">
<style>
  :root {
    --page-bg: #eaeaea;
    --frame-pink: #e8a7a6;
    --rule-white: #feeeee;
    --rose-deep: #c62f6c;
    --rose-mid: #e34197;
    --rose-soft: #eda3c7;
    --plum: #8a3a8c;
    --plum-dark: #6f3583;
    --ink: #1b1b1b;
    --white: #ffffff;
  }
  * { box-sizing: border-box; margin: 0; padding: 0; }
  html, body { width: 1200px; height: 1200px; overflow: hidden; }
  body { background: var(--page-bg); position: relative; font-family: "Roboto", Arial, sans-serif; }

  .flyer {
    position: absolute; left: 196px; top: 30px;
    width: 808px; height: 1140px;
    background: var(--frame-pink);
    padding: 26px;
  }
  .flyer__inner {
    position: relative; width: 100%; height: 100%;
    outline: 2px solid var(--rule-white);
    overflow: hidden;
  }
  .flyer__photo {
    position: absolute; inset: 0;
    background:
      radial-gradient(ellipse 38% 28% at 55% 48%, rgba(246,140,170,0.55), transparent 70%),
      radial-gradient(ellipse 45% 22% at 70% 74%, rgba(140,60,150,0.75), transparent 72%),
      linear-gradient(180deg, var(--rose-deep) 0%, #d03c7c 40%, var(--rose-mid) 75%, #d9409a 100%);
  }
  .flyer__title {
    position: absolute; left: 56px; top: 140px;
    font-family: "Yellowtail", cursive; font-weight: 400;
    font-size: 100px; line-height: 1; color: var(--white);
    white-space: nowrap;
  }
  .highlights { position: absolute; left: 64px; top: 430px; list-style: none; width: 620px; }
  .highlights__item {
    position: relative; padding-left: 40px; margin-bottom: 44px;
    font-weight: 500; font-size: 31px; line-height: 1.12;
    text-transform: uppercase; color: var(--ink);
  }
  .highlights__item::before {
    content: ""; position: absolute; left: 0; bottom: 6px;
    border-left: 18px solid var(--white);
    border-top: 11px solid transparent; border-bottom: 11px solid transparent;
  }

  .contact-band {
    position: absolute; left: 0; right: 0; bottom: 0; height: 178px;
    background: linear-gradient(90deg, rgba(217,58,143,0.9) 0%, rgba(160,58,140,0.92) 55%, var(--plum-dark) 100%);
    display: flex; align-items: center; padding: 0 26px;
  }
  .brand { display: flex; align-items: center; gap: 10px; color: var(--white); font-weight: 700; font-size: 30px; white-space: nowrap; flex: none; }
  .brand__dot { width: 16px; height: 16px; border-radius: 50%; background: var(--white); flex: none; }
  .contacts { margin-left: 30px; display: grid; grid-template-columns: auto auto; column-gap: 24px; row-gap: 14px; }
  .contacts__item { display: flex; align-items: center; gap: 8px; color: var(--white); font-size: 16px; font-weight: 500; white-space: nowrap; }
  .contacts__icon { width: 16px; height: 16px; flex: none; }
</style>
</head>
<body>
  <article class="flyer">
    <div class="flyer__inner">
      <div class="flyer__photo" role="img" aria-label="Yoga instructor seated cross-legged on a mat with arms raised overhead, tinted in pink and plum"></div>

      <h1 class="flyer__title">Yoga By Mirelle</h1>

      <ul class="highlights">
        <li class="highlights__item">E-RYT 200 extensive training with Kestrel Path</li>
        <li class="highlights__item">Social media influencer</li>
        <li class="highlights__item">Offer group, private and corporate yoga classes</li>
      </ul>

      <footer class="contact-band">
        <div class="brand"><span class="brand__dot"></span>Sunlit Mat</div>
        <div class="contacts">
          <div class="contacts__item">
            <svg class="contacts__icon" viewBox="0 0 24 24"><path fill="#fff" d="M6.6 10.8a15 15 0 0 0 6.6 6.6l2.2-2.2a1 1 0 0 1 1-.25 11.4 11.4 0 0 0 3.6.57 1 1 0 0 1 1 1V20a1 1 0 0 1-1 1A17 17 0 0 1 3 4a1 1 0 0 1 1-1h3.5a1 1 0 0 1 1 1c0 1.25.2 2.45.57 3.57a1 1 0 0 1-.25 1z"/></svg>
            555-201-3864
          </div>
          <div class="contacts__item">
            <svg class="contacts__icon" viewBox="0 0 24 24"><circle cx="12" cy="12" r="8" fill="none" stroke="#fff" stroke-width="2"/></svg>
            @sunlitmatcurls
          </div>
          <div class="contacts__item">
            <svg class="contacts__icon" viewBox="0 0 24 24"><rect x="2.5" y="5" width="19" height="14" fill="none" stroke="#fff" stroke-width="1.8"/><path d="M3 6l9 7 9-7" fill="none" stroke="#fff" stroke-width="1.8"/></svg>
            info@yogabymirelle.example
          </div>
          <div class="contacts__item">
            <svg class="contacts__icon" viewBox="0 0 24 24"><circle cx="12" cy="12" r="9" fill="none" stroke="#fff" stroke-width="1.8"/><path d="M3 12h18M12 3c3 3 3 15 0 18M12 3c-3 3-3 15 0 18" fill="none" stroke="#fff" stroke-width="1.6"/></svg>
            www.yogabymirelle.example
          </div>
        </div>
      </footer>
    </div>
  </article>
</body>
</html>
```